GLOW RIDGE 21 DAY Challange

looking to make a poster that needs to be 36" wide x24"tall design graphic . Check out the added file as it is a rough draft of the material I would like it to say.

Phone number 555-302-4418 www.rgchiropractic..com

Adults aged 25-45 high income adults needing to make changes in dies and lose weight

```html
<!DOCTYPE html>
<html lang="en">
<head>
<meta charset="utf-8">
<title>Glow Ridge 21 Day Challange</title>
<link href="https://fonts.googleapis.com/css2?family=Damion&family=Montserrat:wght@500;600;800&family=Arimo:wght@700&display=swap" rel="stylesheet">
<style>
  :root {
    --backdrop: #ecebe8;
    --poster-red: #f2101a;
    --poster-red-deep: #d9000c;
    --accent-yellow: #ffe61a;
    --text-white: #ffffff;
    --text-black: #111111;
  }
  * { box-sizing: border-box; margin: 0; padding: 0; }
  html, body { width: 1200px; height: 1148px; overflow: hidden; }
  body { background: var(--backdrop); position: relative; }

  .poster {
    position: absolute; left: 30px; top: 194px;
    width: 1140px; height: 760px;
    background: radial-gradient(ellipse at 45% 45%, var(--poster-red) 0%, var(--poster-red) 55%, var(--poster-red-deep) 100%);
    display: grid; grid-template-columns: 560px 580px;
  }

  .column-intro {
    display: flex; flex-direction: column; align-items: center;
    padding-top: 62px;
  }
  .column-steps {
    display: flex; flex-direction: column; align-items: center; justify-content: center;
    padding-right: 40px;
  }

  .title { text-align: center; font-weight: normal; }
  .title-name {
    display: block;
    font-family: "Damion", cursive;
    color: var(--accent-yellow);
    font-size: 66px; line-height: 1; letter-spacing: 1px;
  }
  .title-days {
    display: block;
    font-family: "Damion", cursive;
    color: var(--accent-yellow);
    font-size: 136px; line-height: 0.9; margin-top: -4px;
  }
  .title-challenge {
    font-family: "Montserrat", sans-serif; font-weight: 600;
    color: var(--text-white);
    font-size: 20px; letter-spacing: 24px; margin: 22px 0 0 24px;
  }

  .steps { list-style: none; width: 440px; }
  .step { text-align: center; }
  .step-divider { position: relative; height: 30px; }
  .step-divider::before {
    content: ""; position: absolute; left: 0; right: 0; top: 14px;
    border-top: 3px dotted var(--accent-yellow);
  }
  .step-heart { position: absolute; left: 50%; top: 0; width: 32px; height: 30px; transform: translateX(-50%); }
  .step-heart text { font-family: "Montserrat", sans-serif; font-weight: 800; font-size: 15px; fill: var(--text-black); }
  .step-label {
    font-family: "Montserrat", sans-serif; font-weight: 600;
    color: var(--text-white); font-size: 21px; line-height: 40px;
    white-space: nowrap;
  }

  .questions { list-style: none; margin-top: 34px; }
  .question {
    font-family: "Arimo", sans-serif; font-weight: 700;
    color: var(--text-black); font-size: 18px; line-height: 25px;
    display: flex; align-items: center;
  }
  .question::before {
    content: ""; width: 9px; height: 9px; background: var(--text-black);
    margin-right: 16px; flex: none;
  }

  .brand {
    margin-top: 30px; display: flex; align-items: center; gap: 10px;
    font-family: "Montserrat", sans-serif; font-weight: 800;
    color: var(--text-white); font-size: 30px; white-space: nowrap;
  }
  .brand-mark { width: 20px; height: 20px; border-radius: 50%; background: var(--text-white); flex: none; }

  .call-to-action {
    margin-top: 18px;
    font-family: "Montserrat", sans-serif; font-weight: 600;
    color: var(--accent-yellow); font-size: 17px;
  }
  .contact {
    margin-top: 8px; display: flex; gap: 22px;
    font-family: "Montserrat", sans-serif; font-weight: 600;
    color: var(--text-white); font-size: 17px;
  }
</style>
</head>
<body>
<main class="poster">
  <section class="column-intro">
    <h1 class="title">
      <span class="title-name">GLOW RIDGE</span>
      <span class="title-days">21 DAY</span>
    </h1>
    <p class="title-challenge">CHALLANGE</p>

    <ul class="questions">
      <li class="question">Do You Have Allergies</li>
      <li class="question">Need To Lose Weight</li>
      <li class="question">Feel Tired</li>
      <li class="question">Have Neck Or Back Pain</li>
      <li class="question">Contain ..............</li>
    </ul>

    <div class="brand"><span class="brand-mark"></span>RIDGEGATE CHIROPRACTIC</div>
    <p class="call-to-action">CALL TODAY FOR DETAILS</p>
    <p class="contact"><span class="contact-phone">555-302-4418</span><span class="contact-web">www.rgchiropractic..com</span></p>
  </section>

  <section class="column-steps">
    <svg width="0" height="0" style="position:absolute">
      <defs>
        <path id="heart-shape" d="M16 29 C6 21 1 15 1 9 C1 4 5 1 9 1 C12 1 14.5 3 16 5.5 C17.5 3 20 1 23 1 C27 1 31 4 31 9 C31 15 26 21 16 29 Z"/>
      </defs>
    </svg>
    <ol class="steps">
      <li class="step">
        <div class="step-divider"><svg class="step-heart" viewBox="0 0 32 30"><use href="#heart-shape" fill="#ffe61a"/><text x="16" y="18" text-anchor="middle">L</text></svg></div>
        <p class="step-label">LUMA RELAX SUPPLEMENTS</p>
      </li>
      <li class="step">
        <div class="step-divider"><svg class="step-heart" viewBox="0 0 32 30"><use href="#heart-shape" fill="#ffe61a"/><text x="16" y="18" text-anchor="middle">O</text></svg></div>
        <p class="step-label">OMEGA 3 SUPPLEMENTS</p>
      </li>
      <li class="step">
        <div class="step-divider"><svg class="step-heart" viewBox="0 0 32 30"><use href="#heart-shape" fill="#ffe61a"/><text x="16" y="18" text-anchor="middle">V</text></svg></div>
        <p class="step-label">VIT D SUPPLEMENTS</p>
      </li>
      <li class="step">
        <div class="step-divider"><svg class="step-heart" viewBox="0 0 32 30"><use href="#heart-shape" fill="#ffe61a"/><text x="16" y="18" text-anchor="middle">E</text></svg></div>
        <p class="step-label">EAT FRUTS + VEGGIES</p>
      </li>
      <li class="step">
        <div class="step-divider"><svg class="step-heart" viewBox="0 0 32 30"><use href="#heart-shape" fill="#ffe61a"/><text x="16" y="18" text-anchor="middle">K</text></svg></div>
        <p class="step-label">KORA HOMEMADE PROBIOTIC</p>
      </li>
      <li class="step">
        <div class="step-divider"><svg class="step-heart" viewBox="0 0 32 30"><use href="#heart-shape" fill="#ffe61a"/><text x="16" y="18" text-anchor="middle">C</text></svg></div>
        <p class="step-label">CHIROPLACTIC ADJESTMENTS</p>
      </li>
    </ol>
  </section>
</main>
</body>
</html>
```